Divi Theme Wordpress Web Design

Hi,

We have had a Divi theme website running on Wordpress for a few years but need a fresh refresh.

Designs must be possible with standard Divi theme and minimal/no CSS customisation or similar. if this is required please note this in submission. Also, please note mobile and device usage which must be universal.

We have our logo files attached, plus some research and sample sites we have done, plus all of our current collateral. We will need a few examples such as landing (main) page, single blog post and software specific page. See current examples below:

Landing (Main) - http://www.pelrandata.example/inventory-wholesale-manufacturing/

Single Blog Post - http://www.pelrandata.example/why-remote-work-made-break-most-relaxing-ever/

Software Page - http://www.pelrandata.example/software-implementation/tolvek-stock-implementation-and-training/

Target Market(s)

small businesses, small business owners, people who need simple but technical computer help,

Industry/Entity Type

Professional Service

Number of Pages Required

3 page

Requirements
Must have
• see attachment guide
Nice to have
• see attachment guide

```html
<!DOCTYPE html>
<html lang="en">
<head>
<meta charset="utf-8">
<title>PelranData – Inventory Solutions</title>
<link href="https://fonts.googleapis.com/css2?family=Montserrat:wght@300;400;500;600;700&family=Quicksand:wght@400;500;600&display=swap" rel="stylesheet">
<style>
:root{
  --teal:#16b9c4;
  --teal-dark:#0fa3ad;
  --white:#ffffff;
  --ink:#2a2a2a;
  --muted:#555555;
  --panel:#ececec;
  --footer:#1b1b1b;
  --footer-base:#141414;
  --quote:#ededed;
}
*{margin:0;padding:0;box-sizing:border-box}
html,body{width:1200px;height:2211px;overflow:hidden}
body{position:relative;font-family:"Montserrat",sans-serif;color:var(--ink);background:var(--white)}
.abs{position:absolute}

/* hero */
.hero{left:0;top:0;width:1200px;height:554px;overflow:hidden}
.hero-photo{position:absolute;inset:0;background:radial-gradient(ellipse at 55% 60%,#5a544c 0%,#3b3731 45%,#24211e 100%)}
.hero-shade{position:absolute;inset:0;background:rgba(20,18,16,.35)}
.topbar{right:86px;top:10px;display:flex;align-items:center;gap:10px;font-size:10.5px;font-weight:600;color:var(--white)}
.topbar .sep{opacity:.8}
.topbar .social{width:11px;height:11px;border-radius:50%;background:var(--white)}
.brand{left:81px;top:48px;display:flex;align-items:center;gap:10px;font-family:"Montserrat",sans-serif;font-weight:600;font-size:29px;color:var(--white)}
.brand .mark{width:30px;height:30px;border-radius:50%;background:var(--teal)}
.nav{left:451px;top:60px;display:flex;font-size:13.5px;color:var(--white);font-weight:400;letter-spacing:.2px}
.nav a{position:absolute;white-space:nowrap;color:inherit;text-decoration:none}
.nav .active::after{content:"";position:absolute;left:-6px;right:-6px;bottom:-9px;height:2px;background:var(--teal)}
.nav .caret{position:absolute;left:50%;top:20px;width:6px;height:6px;border-right:1.5px solid var(--white);border-bottom:1.5px solid var(--white);transform:translateX(-50%) rotate(45deg)}
.search{left:1100px;top:60px}
.hero-title{left:0;width:1200px;top:214px;text-align:center;font-size:35px;font-weight:600;color:var(--white);letter-spacing:.5px}
.hero-lead{left:0;width:1200px;top:257px;text-align:center;font-size:16.5px;line-height:22px;font-weight:400;color:var(--white)}
.btn{height:34px;border-radius:17px;display:flex;align-items:center;justify-content:center;gap:8px;font-size:13.5px;font-weight:600;color:var(--white)}
.btn-primary{left:461px;top:346px;width:126px;background:var(--teal)}
.btn-ghost{left:613px;top:346px;width:127px;border:1.5px solid var(--white)}
.dots{display:flex;gap:10px;align-items:center}
.hero-dots{left:575px;top:503px}
.hero-dots span{width:8px;height:8px;border-radius:50%;background:var(--white)}
.hero-dots .on{width:13px;height:13px;background:var(--teal);border:2px solid #7fd6dc}

/* bands */
.band{left:0;width:1200px;height:95px;background:var(--teal);display:flex;align-items:center;justify-content:center;font-family:"Quicksand",sans-serif;font-size:22.5px;color:var(--white);font-weight:500}
.band b{font-weight:700}
.band-mark{left:586px;width:28px;height:20px;background:var(--white);border-radius:14px 14px 0 0}
.band-mark::after{content:"";position:absolute;left:8px;top:6px;width:12px;height:12px;border-radius:50%;background:var(--teal)}

/* trust section */
.question{font-size:14px;font-weight:600;line-height:19px;color:var(--ink)}
.q-left{text-align:right;width:300px}
.q-right{width:270px}
.ring{width:98px;height:98px;border-radius:50%;border:1.5px solid var(--teal);background:var(--white);display:flex;align-items:center;justify-content:center}
.ring.filled{background:var(--teal)}
.hub{left:552px;top:770px;width:90px;height:90px;border-radius:50%;background:var(--teal);border:6px solid var(--white)}

/* process */
.process{left:0;top:1079px;width:1200px;height:467px;background:linear-gradient(160deg,#3a3734 0%,#262422 45%,#151413 100%)}
.accordion{left:343px;top:1164px;width:474px}
.acc-head{height:41px;background:var(--teal);display:flex;align-items:center;margin-bottom:6px;color:var(--white);font-family:"Quicksand",sans-serif;font-size:17.5px;font-weight:500;letter-spacing:.3px}
.acc-head .toggle{width:44px;height:100%;display:flex;align-items:center;justify-content:center;background:var(--teal-dark);font-size:22px;font-weight:400;margin-right:20px}
.acc-body{background:var(--panel);padding:20px 14px 18px 13px;font-size:11.5px;line-height:16.5px;color:#333;margin-top:-0px;margin-bottom:6px}

/* testimonial */
.quote-mark{left:282px;top:1662px;font-family:"Montserrat",sans-serif;font-size:190px;line-height:1;color:var(--quote);font-weight:700}
.avatar{left:557px;top:1711px;width:86px;height:86px;border-radius:50%;background:radial-gradient(circle at 50% 40%,#b59a85 0%,#7a6a5d 60%,#4e4642 100%)}
.client{left:0;width:1200px;text-align:center}
.client-name{top:1824px;font-size:12.5px;font-weight:700;color:var(--ink)}
.client-role{top:1841px;font-size:12px;color:var(--muted)}
.client-quote{top:1873px;font-size:17px;color:#3a3a3a;font-weight:400}
.t-dots{left:575px;top:1948px;gap:4px}
.t-dots span{width:14px;height:14px;border-radius:50%;background:#333}
.t-dots .on{background:var(--teal)}

/* footer */
.footer{left:0;top:2006px;width:1200px;height:205px;background:var(--footer)}
.footer-base{left:0;top:2145px;width:1200px;height:66px;background:var(--footer-base)}
.footer-brand{left:81px;top:2062px;font-size:24px;color:#b9b9b9;gap:9px}
.footer-brand .mark{width:26px;height:26px;background:#8a8a8a}
.f-label{font-size:12.5px;color:var(--white);letter-spacing:.3px}
.f-phone{left:467px;top:2065px;font-size:22px;font-weight:700;color:var(--teal)}
.f-social{left:685px;top:2071px;gap:9px}
.f-social span{width:37px;height:37px;border-radius:50%;border:2px solid var(--white)}
.subscribe{left:920px;top:2074px;width:200px;height:31px;background:#050505;color:#8a8a8a;font-size:11px;padding:9px 11px}
.to-top{left:1076px;top:2126px;width:44px;height:44px;border-radius:50%;background:var(--teal);display:flex;align-items:center;justify-content:center}
.copyright{left:0;width:1200px;top:2172px;text-align:center;font-size:12px;color:#cfcfcf}
</style>
</head>
<body>

<section class="hero abs">
  <div class="hero-photo" role="img" aria-label="Photo of hands typing on a laptop at a desk with charts, a calculator, a tablet and a cup of tea"></div>
  <div class="hero-shade"></div>
</section>

<div class="topbar abs">
  <svg width="12" height="12" viewBox="0 0 24 24"><path fill="#fff" d="M6.6 10.8a15 15 0 0 0 6.6 6.6l2.2-2.2c.3-.3.7-.4 1-.2 1.1.4 2.3.6 3.6.6.6 0 1 .4 1 1V20c0 .6-.4 1-1 1A17 17 0 0 1 3 4c0-.6.4-1 1-1h3.5c.6 0 1 .4 1 1 0 1.3.2 2.5.6 3.6.1.3 0 .7-.2 1z"/></svg>
  <span>+61 3 9555 0142 (AU) . +1 (555) 010 4477 (USA)</span><span class="sep">|</span>
  <svg width="14" height="10" viewBox="0 0 14 10"><rect x="0.5" y="0.5" width="13" height="9" fill="none" stroke="#fff"/><path d="M0.5 0.5 7 6l6.5-5.5" fill="none" stroke="#fff"/></svg>
  <span>enquiries@pelrandata.example</span><span class="sep">|</span>
  <span class="social"></span><span class="social"></span><span class="social"></span>
</div>

<div class="brand abs"><span class="mark"></span>PelranData</div>

<nav class="nav abs">
  <a class="active" style="left:0">HOME</a>
  <a style="left:98px">ABOUT US<span class="caret"></span></a>
  <a style="left:218px">BLOG</a>
  <a style="left:311px">SOFTWARE SOLUTIONS<span class="caret"></span></a>
  <a style="left:515px">CONTACT US</a>
</nav>
<svg class="search abs" width="16" height="16" viewBox="0 0 16 16"><circle cx="6.5" cy="6.5" r="4.8" fill="none" stroke="#fff" stroke-width="2"/><path d="M10 10l4.5 4.5" stroke="#fff" stroke-width="2.4" stroke-linecap="round"/></svg>

<h1 class="hero-title abs">OUR LEDGRA ADD-ON SOLUTIONS</h1>
<p class="hero-lead abs">help ambitious businesses who want to take control of their inventory<br>by removing the guess work and enabling them<br>to make better decisions.</p>
<div class="btn btn-primary abs">Read More
  <svg width="14" height="10" viewBox="0 0 14 10"><path d="M1 5h11M8 1l4 4-4 4" fill="none" stroke="#fff" stroke-width="1.6"/></svg></div>
<div class="btn btn-ghost abs">About Us
  <svg width="14" height="10" viewBox="0 0 14 10"><path d="M1 5h11M8 1l4 4-4 4" fill="none" stroke="#fff" stroke-width="1.6"/></svg></div>
<div class="dots hero-dots abs"><span class="on"></span><span></span><span></span></div>

<div class="band abs" style="top:554px">Do you&nbsp;<b>REALLY</b>&nbsp;trust your inventory system?</div>
<div class="band-mark abs" style="top:629px"></div>

<p class="question q-left abs" style="left:132px;top:751px">Are those stock levels accurate?</p>
<p class="question q-left abs" style="left:132px;top:864px">How many do we need to order?</p>
<p class="question q-right abs" style="left:763px;top:743px">Does the Hobart warehouse have<br>stock?</p>
<p class="question q-right abs" style="left:763px;top:855px">Why have we sold so much of that<br>product?</p>

<div class="ring filled abs" style="left:457px;top:710px">
  <svg width="44" height="44" viewBox="0 0 44 44" fill="none" stroke="#fff" stroke-width="2"><path d="M4 40h36"/><rect x="9" y="22" width="5" height="18"/><rect x="17" y="12" width="5" height="28"/><rect x="25" y="18" width="5" height="22"/><rect x="33" y="8" width="5" height="32"/></svg>
</div>
<div class="ring abs" style="left:639px;top:710px">
  <svg width="44" height="48" viewBox="0 0 44 48" fill="none" stroke="#16b9c4" stroke-width="2.5"><rect x="10" y="4" width="24" height="40"/><rect x="15" y="10" width="6" height="6" fill="#16b9c4"/><rect x="23" y="10" width="6" height="6" fill="#16b9c4"/><rect x="15" y="19" width="6" height="6" fill="#16b9c4"/><rect x="23" y="19" width="6" height="6" fill="#16b9c4"/><path d="M4 44h36M19 44v-9h6v9"/></svg>
</div>
<div class="ring abs" style="left:457px;top:822px">
  <svg width="54" height="46" viewBox="0 0 54 46" fill="none" stroke="#16b9c4" stroke-width="2.5"><rect x="3" y="3" width="48" height="32" rx="2"/><path d="M22 35v6M32 35v6M16 43h22"/></svg>
</div>
<div class="ring abs" style="left:639px;top:822px">
  <svg width="50" height="50" viewBox="0 0 50 50" fill="none" stroke="#16b9c4" stroke-width="2.2"><path d="M4 6h42M7 6v28h36V6M25 34v6M25 40l-8 8M25 40l8 8"/><circle cx="25" cy="20" r="8"/><path d="M25 12v8h8"/></svg>
</div>
<div class="hub abs"></div>

<div class="band abs" style="top:985px">Our Process</div>
<div class="band-mark abs" style="top:1060px"></div>

<section class="process abs" role="img" aria-label="Dimmed photo of hands typing on a laptop keyboard"></section>
<div class="accordion abs">
  <div class="acc-head"><span class="toggle">-</span>SCOPING</div>
  <div class="acc-body">Lorem Ipsum is simply dummy text of the printing and typesetting industry. Lorem Ipsum has been the industry's standard dummy text ever since the 1500s, when an unknown printer took a galley of type and scrambled it to make a type specimen book.</div>
  <div class="acc-head"><span class="toggle">+</span>IMPLEMENTATION</div>
  <div class="acc-head"><span class="toggle">+</span>TRAINING</div>
  <div class="acc-head"><span class="toggle">+</span>SUPPORT -Long term (Ongoing)</div>
</div>

<div class="band abs" style="top:1546px">Working with leading lights</div>
<div class="band-mark abs" style="top:1621px"></div>

<div class="quote-mark abs">&ldquo;</div>
<div class="avatar abs" role="img" aria-label="Portrait photo of the client"></div>
<p class="client client-name abs">Martin Kellaway</p>
<p class="client client-role abs">Director, Brightfold Partners</p>
<p class="client client-quote abs">Fantastic service and a focus on ensuring value is delivered in a timely manner.</p>
<div class="dots t-dots abs"><span class="on"></span><span></span><span></span></div>

<footer class="footer abs"></footer>
<div class="footer-base abs"></div>
<div class="brand footer-brand abs"><span class="mark"></span>PelranData</div>
<svg class="abs" style="left:378px;top:2054px" width="32" height="32" viewBox="0 0 24 24"><path fill="#fff" d="M6.6 10.8a15 15 0 0 0 6.6 6.6l2.2-2.2c.3-.3.7-.4 1-.2 1.1.4 2.3.6 3.6.6.6 0 1 .4 1 1V20c0 .6-.4 1-1 1A17 17 0 0 1 3 4c0-.6.4-1 1-1h3.5c.6 0 1 .4 1 1 0 1.3.2 2.5.6 3.6.1.3 0 .7-.2 1z"/></svg>
<p class="f-label abs" style="left:423px;top:2050px">CALL US NOW!</p>
<p class="f-phone abs">123-123-1234</p>
<p class="f-label abs" style="left:685px;top:2050px">FOLLOW US!</p>
<div class="dots f-social abs"><span></span><span></span><span></span></div>
<p class="f-label abs" style="left:920px;top:2050px">SUBSCRIBE!</p>
<div class="subscribe abs">Enter Email</div>
<div class="to-top abs"><svg width="18" height="10" viewBox="0 0 18 10"><path d="M1 9l8-8 8 8" fill="none" stroke="#fff" stroke-width="1.6"/></svg></div>
<p class="copyright abs">All Copyrights Reserved by pelrandata</p>

</body>
</html>
```